Exciting Wordpress Project: New Consulting Firm

A wordpress design is needed for my new consulting company, Brellow Advisory.

The site should have a modern feel to it and use the colour scheme from the attached 3 vector files.

I only know a little about Wordpress but the site should be mobile friendly.

The following menu options should be created:
1. Home
2. Brellow service lines (with sub-menus)
3. Our people
4. Brellow case studies
5. The Brellow story
6. Contact Brellow
Updates

Project Deadline Extended
Reason: Allow just one or two more designs to come in before deciding.

Target Market(s)

Government departments and medium private sector organisations

Industry/Entity Type

It Company

Requirements
Must have
• 1. Inclue Brellow logo at top of each page
2. Slider on the home page
3. Global navigation
4. Drop down navigation
5. Social media links
6. Search and contact details at the top of the home page
7. Home page to fit on one screen
8. Terms & Conditions, Privacy Policy at the bottom of the home page
9. Newsletter (i.e. postwren) subscription on home page
Nice to have
• 1. Background watermark from the Brellow logo
2. A layout similar to the photo attached - however open to different ideas

```html
<!DOCTYPE html>
<html lang="en">
<head>
<meta charset="utf-8">
<title>Brellow Advisory</title>
<link rel="stylesheet" href="https://fonts.googleapis.com/css2?family=Roboto:wght@100;300;400;500;700&display=swap">
<style>
:root{
  --slate:#5f6062;
  --slate-dark:#4e4f51;
  --blue:#3fa6dd;
  --blue-deep:#2c8fc6;
  --ink:#333436;
  --paper:#f4f6f9;
  --muted:#9a9c9f;
  --black:#0b0b0b;
  --white:#ffffff;
  --suit:#c9c7c4;
  --suit-light:#dedcd9;
}
*{box-sizing:border-box;margin:0;padding:0}
html,body{width:1200px;height:890px;overflow:hidden}
body{font-family:"Roboto",Arial,sans-serif;background:var(--paper);position:relative;color:var(--ink)}
a{color:inherit;text-decoration:none}

.top-strip{position:absolute;left:0;top:0;width:1200px;height:8px;background:var(--slate)}
.site-header{position:absolute;left:0;top:8px;width:1200px;height:121px;background:linear-gradient(90deg,#eef1f5,#fbfcfd 50%,#eef1f5)}
.brand{position:absolute;left:200px;top:30px;color:var(--slate);font-weight:500}
.brand-name{display:block;font-size:46px;letter-spacing:1px;line-height:46px}
.brand-sub{display:block;font-size:14px;letter-spacing:19px;line-height:20px;margin-top:4px}

.contact-pill{position:absolute;left:808px;top:6px;width:192px;height:40px;display:flex;align-items:center}
.contact-pill .phone{width:40px;height:40px;border-radius:50%;background:#e4e8ee;border:2px solid #d7dde5;display:flex;align-items:center;justify-content:center;z-index:1}
.contact-pill .label{margin-left:-6px;height:24px;padding:0 8px 0 14px;background:#e4e8ee;border:1px solid #d7dde5;font-size:12px;color:#555;display:flex;align-items:center;white-space:nowrap}

.search-box{position:absolute;left:790px;top:61px;width:210px;height:33px;background:#e3e8ef;border-radius:3px;padding:4px}
.search-box .field{position:absolute;left:5px;top:5px;width:143px;height:23px;background:var(--white);font-size:10.5px;color:#777;padding:6px 7px}
.search-box .go{position:absolute;left:155px;top:5px;width:50px;height:22px;background:var(--blue);border-radius:3px;color:var(--white);font-size:10.5px;text-align:center;line-height:22px}

.main-nav{position:absolute;left:0;top:129px;width:1200px;height:50px;background:var(--slate)}
.main-nav ul{list-style:none;position:absolute;left:200px;top:0;height:50px;display:flex}
.main-nav li{height:50px;line-height:50px;font-size:14.5px;font-weight:300;color:#e4e5e6;text-align:center;border-right:1px dotted #7d7e80;letter-spacing:-.3px}
.main-nav li:last-child{border-right:none}
.main-nav li.active{background:var(--blue);color:#1f3140;font-weight:400}

.hero{position:absolute;left:198px;top:179px;width:804px;height:353px}
.hero-visual{position:absolute;inset:0;background:
  linear-gradient(180deg,rgba(244,246,249,0) 70%,var(--paper) 100%),
  linear-gradient(90deg,#eceef1 0%,#e2e4e7 30%,#d9dbde 55%,#e3e5e8 80%,#eceef1 100%)}
.hero-figure{position:absolute;left:42px;top:12px;width:290px;height:341px;border-radius:120px 120px 0 0;
  background:linear-gradient(180deg,#d7d4d1 0%,var(--suit) 45%,var(--suit-light) 85%,rgba(222,220,217,0) 100%)}

.headline{position:absolute;right:4px;text-align:right;white-space:nowrap}
.line-one{top:120px;width:484px;height:64px;background:var(--blue);padding-right:16px;font-size:43px;line-height:64px;letter-spacing:-1.8px}
.line-one .soft{font-weight:300;color:#2e3f4c}
.line-one .strong{font-weight:700;color:var(--white)}
.line-two{top:189px;width:276px;height:62px;background:var(--slate);padding-right:16px;font-size:43px;line-height:62px;letter-spacing:-1.8px}
.line-two .soft{font-weight:300;color:#b7b8ba}
.line-two .strong{font-weight:700;color:var(--white)}
.line-three{top:253px;right:18px;font-size:44px;font-weight:100;color:#111;letter-spacing:-2px;line-height:50px}

.welcome{position:absolute;left:200px;top:532px;width:802px;height:138px;background:linear-gradient(90deg,#dfeaf5 0%,#f3f6fa 40%,#edf2f8 100%);border:2px solid #f8fafc;box-shadow:0 0 3px rgba(0,0,0,.08)}
.welcome-title{position:absolute;left:10px;top:32px;font-size:58px;font-weight:100;color:var(--blue);letter-spacing:-3px;line-height:70px}
.welcome-text{position:absolute;left:266px;top:13px;width:526px;font-size:10.8px;line-height:17.6px;color:#5c5d60}
.read-more{position:absolute;left:267px;top:94px;width:80px;height:26px;background:var(--slate);color:var(--white);font-size:11.5px;line-height:26px;text-align:center;border-radius:2px}

.site-footer{position:absolute;left:0;top:690px;width:1200px;height:143px;background:var(--slate)}
.footer-links{position:absolute;left:202px;top:14px;list-style:none}
.footer-links li{font-size:12px;color:var(--white);line-height:20px}
.newsletter{position:absolute;left:461px;top:12px;width:280px}
.newsletter h3{font-size:18px;font-weight:300;color:var(--blue);letter-spacing:-.3px}
.newsletter h3 b{font-weight:700;color:var(--white)}
.newsletter p{margin-top:15px;font-size:9.3px;line-height:14.5px;color:#a4a6a9;font-weight:300}
.signup{position:absolute;left:1px;top:76px;width:276px;height:39px;background:#3f4042;border-radius:2px}
.signup .field{position:absolute;left:5px;top:5px;width:203px;height:29px;background:var(--white);border:1px solid #ccc;font-size:9px;color:#666;padding:9px 8px}
.signup .btn{position:absolute;left:214px;top:5px;width:57px;height:29px;background:var(--blue);border:1px solid var(--blue-deep);font-size:9px;color:#173b52;text-align:center;line-height:27px}
.news{position:absolute;left:826px;top:12px;width:180px}
.news h3{font-size:19px;font-weight:300;color:var(--blue);letter-spacing:-.3px}
.news-item{position:absolute;left:2px;display:flex}
.news-item .date{width:32px;height:30px;background:var(--blue);color:var(--white);font-size:9px;text-align:center;line-height:10px;padding-top:5px;clip-path:polygon(0 0,75% 0,100% 30%,100% 100%,0 100%)}
.news-item .teaser{margin-left:11px;font-size:9.8px;line-height:13px;color:#d0d1d3;letter-spacing:.4px;font-weight:300}

.bottom-bar{position:absolute;left:0;top:833px;width:1200px;height:57px;background:var(--black)}
.copyright{position:absolute;left:200px;top:22px;font-size:9.8px;color:#8e9093}
.legal{position:absolute;left:487px;top:22px;font-size:9.8px;color:var(--white)}
.legal span{margin:0 8px;color:#ccc}
.social{position:absolute;left:863px;top:14px;display:flex;gap:8px;list-style:none}
.social li{width:29px;height:29px;border-radius:50%;background:var(--white);display:flex;align-items:center;justify-content:center}
</style>
</head>
<body>
<div class="top-strip"></div>

<header class="site-header">
  <a class="brand" href="#"><span class="brand-name">BRELLOW</span><span class="brand-sub">ADVISORY</span></a>
  <div class="contact-pill">
    <span class="phone">
      <svg width="16" height="22" viewBox="0 0 16 22"><path d="M5 1h3l1 5-3 2c1 3 2 5 4 7l3-1 2 4-2 3c-6-1-11-9-11-17z" fill="#6a6c70"/></svg>
    </span>
    <span class="label">Contact Us:&nbsp; 8000 555 014</span>
  </div>
  <div class="search-box"><div class="field">Search...</div><div class="go">Search</div></div>
</header>

<nav class="main-nav">
  <ul>
    <li class="active" style="width:90px">Home</li>
    <li style="width:139px">Brellow Services</li>
    <li style="width:115px">Our People</li>
    <li style="width:171px">Brellow Case Studies</li>
    <li style="width:145px">The Brellow Story</li>
    <li style="width:140px">Contact Brellow</li>
  </ul>
</nav>

<section class="hero">
  <div class="hero-visual" role="img" aria-label="Smiling consultant in a light grey suit with arms crossed, in front of a dotted world map and faint silhouettes of business people">
    <div class="hero-figure"></div>
  </div>
  <div class="headline line-one"><span class="soft">You Will Have </span><span class="strong">Definitely</span></div>
  <div class="headline line-two"><span class="soft">A Good </span><span class="strong">Start</span></div>
  <div class="headline line-three">With Us!</div>
</section>

<section class="welcome">
  <h1 class="welcome-title">Welcome!</h1>
  <p class="welcome-text">Lorem ipsum dolor sit amet, consectetur adipiscing elit. Quisque vestibulum aliquam metus, a elementum massa sodales et. Duis ultricies lorem id dui fermentum blandit. Nulla vel nisi nisl, aliquet vestibulum velit. Nam a pellentesque massa. Cras ut lacus dolor, non volutpat est. Curabitur dignissim congue dui, nec pretium ante tempus sed. Etiam mi purus, dapibus quis imperdiet eget, condimentum sed tortor.</p>
  <a class="read-more" href="#">Read More..</a>
</section>

<footer class="site-footer">
  <ul class="footer-links">
    <li>Home</li><li>Brellow Services</li><li>Our People</li><li>Brellow Case Studies</li><li>The Brellow Story</li><li>Contact Brellow</li>
  </ul>
  <div class="newsletter">
    <h3>Newsletter <b>Sign Up</b></h3>
    <p>Want to keep up to date with all our latest news and information?<br>Enter your email below to be added to our mailing list.</p>
    <div class="signup"><div class="field">Email Address</div><div class="btn">Sign Up</div></div>
  </div>
  <div class="news">
    <h3>News Artical</h3>
    <div class="news-item" style="top:40px"><div class="date">10<br>May</div><div class="teaser">Lorem ipsum dolor sit amet,<br>consectetur adipiscing elit.</div></div>
    <div class="news-item" style="top:85px"><div class="date">10<br>May</div><div class="teaser">Lorem ipsum dolor sit amet,<br>consectetur adipiscing elit.</div></div>
  </div>
</footer>

<div class="bottom-bar">
  <div class="copyright">© Copyright 2013 BRELLOW ADVISORY - All Rights Reserved</div>
  <div class="legal">Privacy Policy<span>|</span>Terms &amp; Conditions</div>
  <ul class="social">
    <li aria-label="Email us">
      <svg width="15" height="11" viewBox="0 0 15 11"><rect x="1" y="1" width="13" height="9" fill="none" stroke="#111" stroke-width="1.6"/><path d="M1 1l6.5 5L14 1" fill="none" stroke="#111" stroke-width="1.6"/></svg>
    </li>
    <li aria-label="Chat with us">
      <svg width="15" height="14" viewBox="0 0 15 14"><path d="M1 1h13v8H6l-3 3V9H1z" fill="#111"/></svg>
    </li>
    <li aria-label="RSS feed">
      <svg width="14" height="14" viewBox="0 0 14 14"><circle cx="2.5" cy="11.5" r="2" fill="#111"/><path d="M1 6a7 7 0 0 1 7 7M1 1a12 12 0 0 1 12 12" stroke="#111" stroke-width="2.2" fill="none"/></svg>
    </li>
    <li aria-label="Share">
      <svg width="14" height="14" viewBox="0 0 14 14"><circle cx="11" cy="3" r="2.2" fill="#111"/><circle cx="3" cy="7" r="2.2" fill="#111"/><circle cx="11" cy="11" r="2.2" fill="#111"/><path d="M11 3L3 7l8 4" stroke="#111" stroke-width="1.4" fill="none"/></svg>
    </li>
  </ul>
</div>
</body>
</html>
```